Painting Contractor Business Card Design

We are looking for a cool, bold, modern, polished, business card design. We are a high-end residential painting contractor. Please incorporate our logo and keep with our green/black color scheme. We are interested in seeing 2-sided and 1-sided options. Thank you very much!

Industry/Entity Type

Business

Contact Information for Business Card

Info for the card:
Owen Talsky
mobile 206-555-0193
email owen@kestrowfinish.net
web www.kestrowfinish.net

```html
<!DOCTYPE html>
<html lang="en">
<head>
<meta charset="utf-8">
<title>Kestrow Finish – Business Card</title>
<link rel="stylesheet" href="https://fonts.googleapis.com/css2?family=Montserrat:wght@600&family=Saira+Semi+Condensed:wght@600&family=Roboto:wght@300;400&display=swap">
<style>
  :root {
    --bg: #e9e7e3;
    --paper: #ffffff;
    --ink: #2a2a2a;
    --black: #1c1c1c;
    --green: #7ccb2a;
    --green-deep: #5fb41f;
    --sky: #a9d0ef;
    --icon: #f2cf1c;
    --muted: #5a5a5a;
  }
  * { margin: 0; padding: 0; box-sizing: border-box; }
  html, body { width: 1200px; height: 892px; overflow: hidden; }
  body {
    background: var(--bg);
    display: flex;
    align-items: center;
    justify-content: center;
    gap: 60px;
    font-family: "Roboto", Arial, sans-serif;
  }
  .card {
    position: relative;
    width: 520px;
    height: 297px;
    background: var(--paper);
    overflow: hidden;
    box-shadow: 0 6px 20px rgba(0,0,0,0.18);
  }
  .card-bands { position: absolute; inset: 0; width: 100%; height: 100%; }

  .wordmark {
    display: flex;
    align-items: center;
    gap: 10px;
    font-family: "Montserrat", Arial, sans-serif;
    font-weight: 600;
    color: var(--ink);
    letter-spacing: 0.06em;
    white-space: nowrap;
  }
  .wordmark-square { background: var(--green); flex: none; }

  /* Contact side */
  .card--contact .wordmark {
    position: absolute; top: 42px; right: 30px; font-size: 22px;
  }
  .card--contact .wordmark-square { width: 18px; height: 18px; }

  .contact-list {
    position: absolute; top: 40px; left: 30px;
    list-style: none;
    font-size: 12px; font-weight: 300; color: var(--muted);
  }
  .contact-item { display: flex; align-items: center; gap: 9px; margin-bottom: 7px; }
  .contact-icon {
    width: 15px; height: 15px; background: var(--icon);
    display: flex; align-items: center; justify-content: center;
  }
  .contact-icon svg { width: 10px; height: 10px; }

  .person {
    position: absolute; right: 28px; top: 176px; text-align: right;
  }
  .person-name {
    font-family: "Saira Semi Condensed", Arial, sans-serif;
    font-weight: 600; font-size: 28px; color: var(--black); line-height: 1;
  }
  .person-title {
    font-size: 11px; color: var(--paper); margin-top: 3px; letter-spacing: 0.02em;
  }

  /* Brand side */
  .card--brand .wordmark {
    position: absolute; top: 100px; left: 0; right: 0;
    justify-content: center; font-size: 32px;
  }
  .card--brand .wordmark-square { width: 26px; height: 26px; }
</style>
</head>
<body>

  <section class="card card--contact" aria-label="Business card, contact side">
    <svg class="card-bands" viewBox="0 0 520 297" aria-hidden="true">
      <polygon points="290,165 520,165 520,297 250,297" fill="var(--green)"/>
      <polygon points="0,262 290,262 262,297 0,297" fill="var(--sky)"/>
      <rect x="0" y="232" width="520" height="30" fill="var(--black)"/>
    </svg>

    <ul class="contact-list">
      <li class="contact-item">
        <span class="contact-icon"><svg viewBox="0 0 10 10"><path d="M2 1l2 2-1 1c.5 1.2 1.6 2.3 2.8 2.8l1-1 2 2-1.2 1.2C4.5 8.6 1.4 5.5.8 2.2z" fill="var(--black)"/></svg></span>
        206-555-0193
      </li>
      <li class="contact-item">
        <span class="contact-icon"><svg viewBox="0 0 10 10"><rect x="1" y="2.5" width="8" height="5.5" fill="none" stroke="var(--black)"/><path d="M1 2.5l4 3 4-3" fill="none" stroke="var(--black)"/></svg></span>
        owen@kestrowfinish.net
      </li>
      <li class="contact-item">
        <span class="contact-icon"><svg viewBox="0 0 10 10"><circle cx="5" cy="5" r="3.8" fill="none" stroke="var(--black)"/><path d="M1.2 5h7.6M5 1.2c-2 2.4-2 5.2 0 7.6M5 1.2c2 2.4 2 5.2 0 7.6" fill="none" stroke="var(--black)" stroke-width=".8"/></svg></span>
        www.kestrowfinish.net
      </li>
    </ul>

    <div class="wordmark"><span class="wordmark-square"></span>KESTROWFINISH</div>

    <div class="person">
      <p class="person-name">Owen Talsky</p>
      <p class="person-title">Managing Director</p>
    </div>
  </section>

  <section class="card card--brand" aria-label="Business card, brand side">
    <svg class="card-bands" viewBox="0 0 520 297" aria-hidden="true">
      <rect x="0" y="218" width="520" height="32" fill="var(--black)"/>
      <rect x="0" y="250" width="520" height="47" fill="var(--green)"/>
      <polygon points="0,250 240,250 200,297 0,297" fill="var(--sky)"/>
    </svg>
    <div class="wordmark"><span class="wordmark-square"></span>KESTROWFINISH</div>
  </section>

</body>
</html>
```